Web App Design Project

Need to provide graphical design of 2 web pages according to attached wireframes.

Colors should be adjusted for the 65+ population meaning not too bright.

App logo should be created as well - logo should represent long and good life.

Target Market(s)

65 years old and above

```html
<!DOCTYPE html>
<html lang="en">
<head>
<meta charset="utf-8">
<title>Medications – Walter Brooks</title>
<link href="https://fonts.googleapis.com/css2?family=Source+Sans+3:wght@400;600;700;800&display=swap" rel="stylesheet">
<style>
  :root{
    --navy:#0b3566;
    --blue:#1d5fa3;
    --blue-light:#3f86c9;
    --panel:#e4e6e9;
    --panel-border:#c7cacf;
    --active-border:#6b6e73;
    --ink:#1f1f1f;
    --red:#b3202a;
    --white:#ffffff;
    --nav-bg:#d6d8dc;
    --tile-border:#222222;
  }
  *{box-sizing:border-box;margin:0;padding:0}
  html,body{width:1200px;height:804px;overflow:hidden;background:var(--white)}
  body{font-family:"Source Sans 3",Arial,sans-serif;color:var(--ink);position:relative}
  .abs{position:absolute}

  /* header */
  .app-header{left:0;top:0;width:1200px;height:76px;background:linear-gradient(180deg,var(--blue) 0%,var(--navy) 100%)}
  .brand-mark{left:40px;top:10px;width:56px;height:56px;border-radius:50%;background:var(--white)}
  .user-name{left:162px;top:12px;font-size:40px;font-weight:700;color:var(--white);line-height:50px}
  .search-field{left:670px;top:12px;width:245px;height:54px;background:var(--white);border:3px solid #9aa3ad;font-size:28px;font-weight:600;padding:6px 12px}
  .head-btn{top:12px;height:54px;background:linear-gradient(#fff,#dfe2e6);border:3px solid #9aa3ad;display:flex;align-items:center;justify-content:center;font-size:30px;font-weight:700}
  .btn-search{left:930px;width:56px}
  .btn-help{left:1027px;width:55px}
  .btn-exit{left:1098px;width:90px}

  /* toolbar */
  .section-tab{left:11px;top:85px;width:281px;height:49px;border:3px solid #7a7d82;border-bottom:none;border-radius:10px 10px 0 0;background:var(--panel);font-size:32px;font-weight:700;color:var(--navy);text-align:center;line-height:46px}
  .add-med{left:338px;top:87px;display:flex;align-items:center;gap:12px;font-size:28px;font-weight:700}
  .settings{left:1113px;top:85px}

  /* medication rows */
  .time-tab{left:11px;width:281px;background:var(--panel);border:3px solid var(--panel-border);border-radius:8px;display:flex;align-items:center;gap:10px;padding-left:40px;font-size:26px;font-weight:700;color:#1a2a44}
  .time-tab.active{background:none;border:3px solid var(--active-border);padding:0}
  .active-pill{position:absolute;left:8px;top:10px;width:298px;height:90px}
  .active-label{position:absolute;left:0;top:10px;width:270px;height:90px;display:flex;align-items:center;gap:18px;padding-left:42px;color:var(--white);font-size:27px}
  .med-row{left:300px;width:886px;background:var(--panel);border:3px solid var(--panel-border);border-radius:10px}
  .med-row.active{border:3px solid var(--active-border);border-radius:0 14px 14px 14px}
  .taken-hint{left:345px;top:146px;font-size:15px;font-weight:700}
  .cell{position:absolute;top:50%;transform:translateY(-50%);height:70px;background:var(--white);border:3px solid #4a4c50}
  .cell-check{left:30px;width:74px;display:flex;align-items:center;justify-content:center}
  .cell-name{left:124px;width:443px;font-size:40px;font-weight:800;line-height:64px;padding-left:14px;white-space:nowrap}
  .cell-dose{left:583px;width:72px;font-size:40px;font-weight:800;line-height:64px;text-align:center}
  .cell-pill{left:673px;width:107px;display:flex;align-items:center;justify-content:center}
  .info-btn{position:absolute;left:820px;top:50%;transform:translateY(-50%)}

  /* bottom navigation */
  .nav-rule{left:0;top:618px;width:1200px;height:10px;background:var(--blue)}
  .bottom-nav{left:0;top:628px;width:1200px;height:176px;background:var(--nav-bg)}
  .nav-active-bg{left:0;top:628px;width:167px;height:176px;background:linear-gradient(var(--blue-light),var(--blue))}
  .nav-tile{top:637px;width:160px;height:159px;background:var(--white);border:5px solid var(--tile-border);display:flex;flex-direction:column;align-items:center;justify-content:flex-end;padding-bottom:6px;font-size:17px;font-weight:700;text-align:center;line-height:19px}
  .nav-tile.active{left:14px;width:145px;border:3px solid #8aa9c9}
  .nav-art{margin-bottom:auto;margin-top:10px}
  .art-block{border-radius:10px}
</style>
</head>
<body>

<header>
  <div class="abs app-header"></div>
  <div class="abs brand-mark" aria-hidden="true"></div>
  <div class="abs user-name">Walter Brooks</div>
  <div class="abs search-field">Search</div>
  <div class="abs head-btn btn-search" aria-label="Search">
    <svg width="38" height="38" viewBox="0 0 38 38"><circle cx="23" cy="14" r="10" fill="none" stroke="var(--blue)" stroke-width="4"/><line x1="16" y1="21" x2="4" y2="34" stroke="var(--blue)" stroke-width="6" stroke-linecap="round"/></svg>
  </div>
  <div class="abs head-btn btn-help">?</div>
  <div class="abs head-btn btn-exit">Exit</div>
</header>

<div class="abs section-tab">Medications</div>
<div class="abs add-med">
  <svg width="44" height="44" viewBox="0 0 44 44"><circle cx="22" cy="22" r="20" fill="#dfe4ea" stroke="#8b98a6" stroke-width="2"/><path d="M22 10v24M10 22h24" stroke="var(--blue)" stroke-width="6"/></svg>
  Add Medication
</div>
<svg class="abs settings" width="50" height="50" viewBox="0 0 50 50" aria-label="Settings">
  <g fill="var(--blue)"><circle cx="25" cy="25" r="16"/>
  <g id="tooth"><rect x="21" y="2" width="8" height="10" rx="2"/></g>
  <use href="#tooth" transform="rotate(45 25 25)"/><use href="#tooth" transform="rotate(90 25 25)"/><use href="#tooth" transform="rotate(135 25 25)"/><use href="#tooth" transform="rotate(180 25 25)"/><use href="#tooth" transform="rotate(225 25 25)"/><use href="#tooth" transform="rotate(270 25 25)"/><use href="#tooth" transform="rotate(315 25 25)"/></g>
  <circle cx="25" cy="25" r="7" fill="var(--white)"/>
</svg>

<svg width="0" height="0" style="position:absolute">
  <defs>
    <symbol id="tick" viewBox="0 0 60 50"><path d="M4 26 L22 44 L56 6 L24 32 Z" fill="var(--red)"/></symbol>
    <symbol id="info" viewBox="0 0 40 40"><circle cx="20" cy="20" r="19" fill="var(--blue)"/><circle cx="20" cy="11" r="3.5" fill="#fff"/><rect x="16.5" y="17" width="7" height="15" rx="2" fill="#fff"/></symbol>
  </defs>
</svg>

<!-- Morning -->
<div class="abs time-tab active" style="top:145px;height:110px">
  <svg class="active-pill" viewBox="0 0 298 90"><path d="M10 0H262L298 45L262 90H10A10 10 0 0 1 0 80V10A10 10 0 0 1 10 0Z" fill="var(--navy)"/></svg>
  <div class="active-label">
    <svg width="52" height="30" viewBox="0 0 52 30"><path d="M12 22a14 14 0 0 1 28 0Z" fill="#fff"/><g stroke="#fff" stroke-width="3"><line x1="26" y1="0" x2="26" y2="5"/><line x1="10" y1="6" x2="13" y2="10"/><line x1="42" y1="6" x2="39" y2="10"/><line x1="2" y1="22" x2="50" y2="22"/><line x1="10" y1="28" x2="42" y2="28"/></g></svg>
    Morning
  </div>
</div>
<div class="abs taken-hint">Mark as Taken</div>
<div class="abs med-row active" style="top:145px;height:110px">
  <div class="cell cell-check"><svg width="52" height="44"><use href="#tick"/></svg></div>
  <div class="cell cell-name">Medication_01 Name</div>
  <div class="cell cell-dose">4x</div>
  <div class="cell cell-pill"><svg width="92" height="36" viewBox="0 0 92 36"><rect x="2" y="4" width="88" height="28" rx="14" fill="var(--blue-light)"/><path d="M16 4H46V32H16A14 14 0 0 1 16 4Z" fill="var(--red)"/></svg></div>
  <svg class="info-btn" width="40" height="40"><use href="#info"/></svg>
</div>

<!-- Noon -->
<div class="abs time-tab" style="top:268px;height:106px">
  <svg width="40" height="40" viewBox="0 0 40 40"><circle cx="20" cy="20" r="9" fill="var(--blue)"/><g stroke="var(--blue)" stroke-width="3"><line x1="20" y1="2" x2="20" y2="8"/><line x1="20" y1="32" x2="20" y2="38"/><line x1="2" y1="20" x2="8" y2="20"/><line x1="32" y1="20" x2="38" y2="20"/><line x1="7" y1="7" x2="11" y2="11"/><line x1="29" y1="29" x2="33" y2="33"/><line x1="33" y1="7" x2="29" y2="11"/><line x1="11" y1="29" x2="7" y2="33"/></g></svg>
  Noon
</div>
<div class="abs med-row" style="top:268px;height:106px">
  <div class="cell cell-check"><svg width="52" height="44"><use href="#tick"/></svg></div>
  <div class="cell cell-name">Medication_03 Name</div>
  <div class="cell cell-dose">2x</div>
  <div class="cell cell-pill"><svg width="54" height="54" viewBox="0 0 54 54"><circle cx="27" cy="27" r="24" fill="var(--blue)"/><path d="M27 3A24 24 0 0 0 27 51Z" fill="var(--red)"/></svg></div>
  <svg class="info-btn" width="40" height="40"><use href="#info"/></svg>
</div>

<!-- Afternoon -->
<div class="abs time-tab" style="top:386px;height:106px;padding-left:26px">
  <svg width="62" height="40" viewBox="0 0 62 40"><circle cx="36" cy="16" r="10" fill="var(--blue)"/><g stroke="var(--blue)" stroke-width="3"><line x1="36" y1="0" x2="36" y2="4"/><line x1="50" y1="16" x2="54" y2="16"/><line x1="47" y1="5" x2="44" y2="8"/><line x1="25" y1="5" x2="28" y2="8"/></g><path d="M4 36a8 8 0 0 1 8-10a10 10 0 0 1 18-2a8 8 0 0 1 14 4a6 6 0 0 1 6 8Z" fill="#5b93c9"/></svg>
  Afternoon
</div>
<div class="abs med-row" style="top:386px;height:106px">
  <div class="cell cell-check"><svg width="52" height="44"><use href="#tick"/></svg></div>
  <div class="cell cell-name">Medication_03 Name</div>
  <div class="cell cell-dose">4x</div>
  <div class="cell cell-pill"><svg width="86" height="50" viewBox="0 0 86 50"><g transform="rotate(-22 43 25)"><rect x="4" y="12" width="78" height="26" rx="13" fill="var(--blue)"/><path d="M17 12H43V38H17A13 13 0 0 1 17 12Z" fill="var(--red)"/></g></svg></div>
  <svg class="info-btn" width="40" height="40"><use href="#info"/></svg>
</div>

<!-- Night -->
<div class="abs time-tab" style="top:506px;height:106px;padding-left:62px">
  <svg width="36" height="40" viewBox="0 0 36 40"><path d="M26 2A19 19 0 1 0 34 34A16 16 0 0 1 26 2Z" fill="var(--blue)"/></svg>
  Night
</div>
<div class="abs med-row" style="top:506px;height:106px">
  <div class="cell cell-check"><svg width="52" height="44"><use href="#tick"/></svg></div>
  <div class="cell cell-name">Medication_04 Name</div>
  <div class="cell cell-dose">2x</div>
  <div class="cell cell-pill"><svg width="92" height="36" viewBox="0 0 92 36"><rect x="1" y="2" width="90" height="32" rx="4" fill="var(--blue-light)" stroke="var(--navy)" stroke-width="2"/><g fill="var(--red)"><circle cx="10" cy="11" r="4"/><circle cx="21" cy="11" r="4"/><circle cx="32" cy="11" r="4"/><circle cx="43" cy="11" r="4"/><circle cx="54" cy="11" r="4"/><circle cx="65" cy="11" r="4"/><circle cx="76" cy="11" r="4"/><circle cx="10" cy="25" r="4"/><circle cx="21" cy="25" r="4"/><circle cx="32" cy="25" r="4"/><circle cx="43" cy="25" r="4"/><circle cx="54" cy="25" r="4"/><circle cx="65" cy="25" r="4"/><circle cx="76" cy="25" r="4"/></g></svg></div>
  <svg class="info-btn" width="40" height="40"><use href="#info"/></svg>
</div>

<!-- Bottom navigation -->
<nav>
  <div class="abs nav-rule"></div>
  <div class="abs bottom-nav"></div>
  <div class="abs nav-active-bg"></div>
  <div class="abs nav-tile active">
    <svg class="nav-art" width="130" height="100" viewBox="0 0 130 100"><g transform="rotate(-30 40 50)"><rect x="20" y="6" width="40" height="90" rx="20" fill="#e4e4e4"/><path d="M20 51H60V76A20 20 0 0 1 20 76Z" fill="var(--red)"/></g><circle cx="95" cy="58" r="28" fill="#e4e4e4"/><path d="M95 30A28 28 0 0 0 95 86Z" fill="var(--red)"/></svg>
    Medications
  </div>
  <div class="abs nav-tile" style="left:177px">
    <div class="nav-art art-block" role="img" aria-label="Thermometer icon" style="width:70px;height:95px;background:linear-gradient(135deg,#7fb2e0,#c0414a)"></div>
    Home<br>Measurements
  </div>
  <div class="abs nav-tile" style="left:349px">
    <svg class="nav-art" width="100" height="90" viewBox="0 0 100 90"><rect x="4" y="10" width="92" height="76" rx="8" fill="var(--blue)"/><rect x="4" y="10" width="92" height="18" rx="6" fill="var(--navy)"/><g fill="#fff"><rect x="14" y="36" width="14" height="10"/><rect x="32" y="36" width="14" height="10"/><rect x="50" y="36" width="14" height="10"/><rect x="68" y="36" width="14" height="10"/><rect x="14" y="52" width="14" height="10"/><rect x="32" y="52" width="14" height="10"/><rect x="50" y="52" width="14" height="10"/><rect x="68" y="52" width="14" height="10"/><rect x="14" y="68" width="14" height="10"/><rect x="32" y="68" width="14" height="10"/></g><rect x="24" y="2" width="8" height="16" rx="3" fill="#555"/><rect x="68" y="2" width="8" height="16" rx="3" fill="#555"/></svg>
    My Schedule
  </div>
  <div class="abs nav-tile" style="left:521px">
    <div class="nav-art art-block" role="img" aria-label="Stethoscope icon" style="width:80px;height:85px;background:linear-gradient(135deg,#c0414a,#2b6fb3)"></div>
    Lab Tests<br>Results
  </div>
  <div class="abs nav-tile" style="left:689px">
    <svg class="nav-art" width="90" height="95" viewBox="0 0 90 95"><rect x="8" y="6" width="62" height="86" rx="4" fill="var(--navy)"/><rect x="14" y="14" width="50" height="72" fill="#fff"/><g stroke="var(--red)" stroke-width="3" fill="none"><path d="M18 24l4 4 7-8"/><path d="M18 40l4 4 7-8"/><path d="M18 56l4 4 7-8"/></g><g stroke="var(--navy)" stroke-width="4"><line x1="34" y1="26" x2="58" y2="26"/><line x1="34" y1="42" x2="58" y2="42"/><line x1="34" y1="58" x2="58" y2="58"/><line x1="20" y1="74" x2="58" y2="74"/></g><line x1="50" y1="80" x2="86" y2="36" stroke="var(--red)" stroke-width="6"/></svg>
    Checkups &amp;<br>Procedures
  </div>
  <div class="abs nav-tile" style="left:863px">
    <div class="nav-art art-block" role="img" aria-label="Profile card icon" style="width:118px;height:76px;margin-top:20px;background:linear-gradient(180deg,#3f86c9,#1d5fa3)"></div>
    My Profile
  </div>
  <div class="abs nav-tile" style="left:1033px">
    <div class="nav-art art-block" role="img" aria-label="Care provider icon" style="width:70px;height:92px;background:linear-gradient(180deg,#5b93c9,#0b3566)"></div>
    My Health Care<br>Providers
  </div>
</nav>

</body>
</html>
```